Simple Logo Design for Semi-Clear Plastic Frosted Card stock

Create a business card on frosted plastic. compliment existing logo elements with a tree trunk, roots, or seed at the lower half and the full logo both on the front.

Contact information will go on a solid portion of the back of this design since this card stock is semi-transparent.

It is important to consider this plastic card stock medium in your design. I found helpful tips and guides listed at velnacard.example: be careful to understand ink printed on plastic cards cannot have too much of a consistent print area or risks peeling and fine lines can easily scratch off.
Updates

2" x 3.5" 20PT Clear Plastic Business cards with Round corners Please get info or templates here: https://www.velnacard.example/product-detail/2-x-35-20pt-clear-plastic-business-cards-with-round-corners

Target Market(s)

Not for profit- religion

Industry/Entity Type

Business

Contact Information for Business Card

Must include complementary elements to the existing logo

Font styles to use
Decorative

Colors
000000

Requirements
Must have
• Elements of community, nature and oneness. Such as: seed, roots, tree trunk, etc.
• Three lines of space on the back for Name, Title, Phone Number.
Nice to have
• I like a light use of decorative elements
Should not have
• No eyes, from faces or animals.

```html
<!DOCTYPE html>
<html lang="en">
<head>
<meta charset="utf-8">
<title>Rootwell Commons – Business Card</title>
<link rel="stylesheet" href="https://fonts.googleapis.com/css2?family=Mulish:wght@400;600;700&display=swap">
<style>
  :root {
    --page-bg: #d8d1c6;
    --frost: #efede8;
    --frost-edge: #e2e0da;
    --teal: #2c6764;
    --teal-deep: #1f5553;
    --leaf: #4f9b34;
    --leaf-light: #6db24a;
    --ink: #2f3b3a;
    --ink-soft: #4a5251;
  }
  * { margin: 0; padding: 0; box-sizing: border-box; }
  html, body {
    width: 969px;
    height: 1200px;
    overflow: hidden;
    background: var(--page-bg);
  }
  .card {
    position: absolute;
    left: 204px;
    top: 98px;
    width: 560px;
    height: 1004px;
    border-radius: 38px;
    background: linear-gradient(180deg, var(--frost) 0%, #f2f0ec 60%, var(--frost-edge) 100%);
    overflow: hidden;
    font-family: "Mulish", sans-serif;
    color: var(--ink);
    text-align: center;
  }
  .card__header {
    position: absolute;
    left: 0;
    top: 0;
    width: 560px;
    height: 345px;
  }
  .card__footer {
    position: absolute;
    left: 0;
    bottom: 0;
    width: 560px;
    height: 50px;
  }
  .emblem-area {
    position: absolute;
    left: 156px;
    top: 400px;
    width: 248px;
    height: 152px;
    border-radius: 12px;
    background: linear-gradient(180deg, #7bb85c 0%, #4f9b34 40%, #2c6764 100%);
    opacity: 0.85;
  }
  .brand {
    position: absolute;
    left: 0;
    right: 0;
    top: 572px;
  }
  .brand__name {
    display: inline-flex;
    align-items: center;
    gap: 12px;
    font-weight: 600;
    font-size: 38px;
    letter-spacing: 0.3px;
    color: var(--teal);
    text-transform: uppercase;
  }
  .brand__dot {
    width: 14px;
    height: 14px;
    border-radius: 50%;
    background: var(--leaf);
  }
  .brand__tagline {
    margin-top: 4px;
    font-size: 20px;
    letter-spacing: 0.6px;
    color: var(--ink-soft);
    text-transform: uppercase;
  }
  .divider {
    position: absolute;
    left: 92px;
    top: 668px;
    width: 376px;
    height: 2px;
    background: linear-gradient(90deg, transparent, var(--leaf) 20%, var(--leaf) 80%, transparent);
  }
  .motto {
    position: absolute;
    left: 0;
    right: 0;
    top: 690px;
    font-size: 23px;
    color: var(--ink);
    text-transform: uppercase;
  }
  .contact {
    position: absolute;
    left: 0;
    right: 0;
    top: 795px;
  }
  .contact__name {
    font-weight: 700;
    font-size: 33px;
    letter-spacing: 0.5px;
    color: var(--teal);
    text-transform: uppercase;
  }
  .contact__title {
    margin-top: 4px;
    font-size: 25px;
    color: var(--ink-soft);
  }
  .contact__phone {
    margin-top: 24px;
    font-size: 24px;
    color: var(--ink-soft);
  }
</style>
</head>
<body>
  <div class="card">
    <svg class="card__header" viewBox="0 0 560 345" role="img" aria-label="Leafy tree canopy with trunks and branches arching over the card top">
      <defs>
        <linearGradient id="canopy" x1="0" y1="0" x2="0" y2="1">
          <stop offset="0" stop-color="#2a6663"/>
          <stop offset="0.45" stop-color="#2f6e60"/>
          <stop offset="0.75" stop-color="#4a9640"/>
          <stop offset="1" stop-color="#9fbfb5"/>
        </linearGradient>
      </defs>
      <path d="M0 0 H560 V292 Q280 232 0 292 Z" fill="url(#canopy)"/>
      <path d="M0 292 Q280 232 560 292 V306 Q280 246 0 306 Z" fill="var(--leaf)"/>
    </svg>

    <div class="emblem-area" role="img" aria-label="Organisation emblem: tree with leafy crown above its trunk"></div>

    <div class="brand">
      <div class="brand__name"><span class="brand__dot"></span>Rootwell Commons</div>
      <div class="brand__tagline">Knowledge, Friendship &amp; Peace</div>
    </div>

    <div class="divider"></div>
    <div class="motto">Together as One Community</div>

    <div class="contact">
      <div class="contact__name">Mara Ellison</div>
      <div class="contact__title">General Manager</div>
      <div class="contact__phone">+555-014-2290</div>
    </div>

    <svg class="card__footer" viewBox="0 0 560 50" aria-hidden="true">
      <path d="M0 50 V40 Q280 -8 560 40 V50 Z" fill="var(--teal)"/>
      <path d="M0 40 Q280 -8 560 40 V34 Q280 -16 0 34 Z" fill="var(--leaf)"/>
    </svg>
  </div>
</body>
</html>
```